Technical building equipment company needs PowerPoint master slide...

Our medium-sized group of companies specializes in equipping commercial properties with large-scale technical systems in the areas of electrical, heating, ventilation, refrigeration and air conditioning. For our uniform corporate identity (CI), we need a PowerPoint master slide for a wide range of operational applications, e.g. company presentations, training courses, etc.
Updates

Urlaub/Ferien

Target Market(s)

Multiple: banks, shareholders, employees, business partners, etc

Industry/Entity Type

Technische Gebäudeausrüstung, Baubranche

Font styles to use
Sans Serif

Colors
0054AA
0677BA
7BADD7
CADEEF
E8F1F8
EB3D1F
EC4F4E
F09395
F8D3D4
FCEDEE

Requirements
Must have
• Films must be usable for a variety of purposes.

```html
<!DOCTYPE html>
<html lang="en">
<head>
<meta charset="utf-8">
<title>Kestra Gruppe – Presentation Master</title>
<link href="https://fonts.googleapis.com/css2?family=Roboto+Condensed:wght@700&family=Montserrat:wght@400;500;600;700;800&display=swap" rel="stylesheet">
<style>
:root{
  --navy:#2d2a8a;
  --red:#e3131e;
  --ink:#333;
  --grey:#6b6b72;
  --rule:#d9d9e2;
  --paper:#ffffff;
  --bg:#cfcfd2;
}
*{box-sizing:border-box;margin:0;padding:0}
html,body{width:1045px;height:1200px;overflow:hidden}
body{background:linear-gradient(180deg,#d6d6d9,#c4c4c8);font-family:Montserrat,sans-serif;position:relative}
.slide{position:absolute;width:321px;height:181px;background:var(--paper);overflow:hidden;box-shadow:0 1px 3px rgba(0,0,0,.25)}
.c1{left:30px}.c2{left:363px}.c3{left:697px}
.r1{top:27px}.r2{top:220px}.r3{top:415px}.r4{top:608px}.r5{top:800px}.r6{top:995px}
.abs{position:absolute}
.brand{position:absolute;top:8px;right:9px;display:flex;align-items:center;gap:3px;font:800 6.5px/0.95 Montserrat,sans-serif;color:var(--navy)}
.brand i{display:block;width:12px;height:12px;border-radius:50%;background:var(--red)}
.on-navy .brand{color:var(--navy)}
.title{position:absolute;left:12px;top:12px;font:700 13px/1 "Roboto Condensed",sans-serif;color:var(--navy)}
.title::after{content:"";display:block;width:40px;height:1.5px;background:var(--red);margin-top:4px}
.title.light{color:#fff}
.foot{position:absolute;left:0;bottom:6px;display:flex;align-items:center;gap:2px;font:500 3.6px Montserrat,sans-serif;letter-spacing:.5px;color:var(--navy)}
.foot::before{content:"";width:16px;height:.6px;background:var(--red)}
.foot::after{content:"";width:4px;height:.6px;background:var(--red)}
.foot.light{color:#fff}
.pg{position:absolute;right:6px;bottom:4px;width:10px;height:10px;border-radius:50%;background:var(--red);color:#fff;font:700 3.5px/10px Montserrat,sans-serif;text-align:center}
.p{font:400 3.5px/1.4 Montserrat,sans-serif;color:var(--grey)}
.p.w{color:#fff}
.p+.p{margin-top:4px}
.panel{position:absolute;top:0;left:0;height:100%;background:var(--navy)}
.photo{position:absolute}
.h-item{font:500 7px/1 Montserrat,sans-serif;color:var(--navy)}
.num{font:700 8px/1 Montserrat,sans-serif;color:var(--red)}
.red{color:var(--red)}
.navy{color:var(--navy)}
.ring{position:absolute;border-radius:50%;border:1.2px solid var(--red);display:flex;align-items:center;justify-content:center;background:#fff}
.cap{font:700 5px/1 Montserrat,sans-serif;color:var(--navy);text-align:center}
.bullet{display:flex;gap:4px;align-items:flex-start}
.bullet b{flex:none;width:0;height:0;border-left:4px solid var(--red);border-top:2.3px solid transparent;border-bottom:2.3px solid transparent;margin-top:1px}
.bullet b.o{border-left-color:var(--navy);opacity:.6}
</style>
</head>
<body>

<!-- 1 Cover -->
<section class="slide c1 r1">
  <div class="photo" role="img" aria-label="Photo of a modern glass office tower against a blue sky" style="left:150px;top:0;width:171px;height:181px;background:linear-gradient(160deg,#dfe9f3 0%,#a9c0d8 45%,#4d6a8c 80%,#2c3f5a 100%)"></div>
  <div class="abs" style="left:12px;top:12px;display:flex;align-items:center;gap:7px">
    <span style="width:34px;height:34px;border-radius:50%;background:var(--red);display:block"></span>
    <span style="font:800 15px/0.95 Montserrat,sans-serif;color:var(--navy)">KESTRA<br>GRUPPE</span>
  </div>
  <div class="abs" style="left:13px;top:97px;font:500 8.5px/1 Montserrat,sans-serif;color:var(--ink)">PRESENTATION</div>
  <div class="abs" style="left:12px;top:107px;font:700 22px/1 'Roboto Condensed',sans-serif;color:var(--red)">BUSINESS</div>
  <div class="abs" style="left:12px;top:129px;font:700 22px/1 'Roboto Condensed',sans-serif;color:var(--navy)">MARKETING</div>
  <div class="abs" style="left:13px;top:157px;font:500 7.5px/1 Montserrat,sans-serif;letter-spacing:2.6px;color:var(--red)">www.kestragruppe.com</div>
</section>

<!-- 2 Contents -->
<section class="slide c2 r1">
  <h2 class="title">Contents</h2>
  <div class="brand"><i></i>KESTRA<br>GRUPPE</div>
  <div class="abs" style="left:28px;top:48px;width:280px;display:grid;grid-template-columns:1fr 1fr;row-gap:14px;column-gap:12px">
    <div style="display:flex;gap:6px"><span class="num">1.</span><div><div class="h-item">Lorem ipsum</div><p class="p" style="margin-top:2px">Lorem ipsum dolor sit amet, consectetuer adipiscing elit, sed diam nonummy nibh euis-</p></div></div>
    <div style="display:flex;gap:6px"><span class="num">2.</span><div><div class="h-item">Lorem ipsum</div><p class="p" style="margin-top:2px">Lorem ipsum dolor sit amet, consectetuer adipiscing elit, sed diam nonummy nibh euismod tincid</p></div></div>
    <div style="display:flex;gap:6px"><span class="num">3.</span><div><div class="h-item">Lorem ipsum</div><p class="p" style="margin-top:2px">Lorem ipsum dolor sit amet, consectetuer adipiscing elit, sed diam nonummy nibh euis-</p></div></div>
    <div style="display:flex;gap:6px"><span class="num">4.</span><div><div class="h-item">Lorem ipsum</div><p class="p" style="margin-top:2px">Lorem ipsum dolor sit amet, consectetuer adipiscing elit, sed diam nonummy nibh euismod tincid</p></div></div>
    <div style="display:flex;gap:6px"><span class="num">5.</span><div><div class="h-item">Lorem ipsum</div><p class="p" style="margin-top:2px">Lorem ipsum dolor sit amet, consectetuer adipiscing elit, sed diam nonummy nibh euis-</p></div></div>
    <div style="display:flex;gap:6px"><span class="num">6.</span><div><div class="h-item">Lorem ipsum</div><p class="p" style="margin-top:2px">Lorem ipsum dolor sit amet, consectetuer adipiscing elit, sed diam nonummy nibh euismod tincid</p></div></div>
  </div>
  <div class="foot">www.kestragruppe.com</div><span class="pg">02</span>
</section>

<!-- 3 Active Intelligence -->
<section class="slide c3 r1">
  <h2 class="title">Active Intelligence</h2>
  <div class="brand"><i></i>KESTRA<br>GRUPPE</div>
  <div class="abs" style="left:12px;top:41px;width:138px">
    <p class="p" style="text-align:justify">Lorem ipsum dolor sit amet, consectetuer adipiscing elit, sed diam nonummy nibh euismod tincidunt ut laoreet dolore magna aliquam erat volutpat. Ut wisi enim ad minim veniam, quis nostrud exerci tation ullamcorper suscipit lobortis nisl ut aliquip ex ea commodo consequat. Duis autem vel eum iriure dolor in hendrerit in vulputate velit esse</p>
    <p class="p" style="text-align:justify">Lorem ipsum dolor sit amet, consectetuer adipiscing elit, sed diam nonummy nibh euismod tincidunt ut laoreet dolore magna aliquam erat volutpat. Ut wisi enim ad minim veniam, quis nostrud exerci tation ullamcorper suscipit lobortis nisl ut aliquip ex ea commodo consequat. Duis autem vel eum iriure dolor in hendrerit in vulputate velit esse</p>
    <div class="bullet" style="margin-top:6px"><b class="o" style="border-left-color:var(--navy);opacity:1"></b><p class="p">Lorem ipsum dolor sit amet, consectetuer adipiscing elit, sed diam nonummy nibh euismod tincidunt ut laoreet dolore magna</p></div>
    <div class="bullet" style="margin-top:6px"><b class="o"></b><p class="p">Lorem ipsum dolor sit amet, consectetuer adipiscing elit, sed diam nonummy nibh euismod tincidunt ut laoreet dolore magna</p></div>
  </div>
  <div class="abs" style="left:163px;top:37px;width:69px;height:1.5px;background:var(--red)"></div>
  <div class="abs" style="left:163px;top:37px;width:1.5px;height:119px;background:var(--red)"></div>
  <div class="abs" style="left:163px;top:155px;width:155px;height:1.5px;background:var(--red)"></div>
  <div class="photo" role="img" aria-label="Photo of colleagues working at a desk with laptops and charts" style="left:167px;top:42px;width:154px;height:110px;background:linear-gradient(135deg,#3a4d66,#8fa3b8 45%,#d9dde2 75%,#5d6e82)"></div>
  <div class="foot">www.kestragruppe.com</div><span class="pg">03</span>
</section>

<!-- 4 Our Company -->
<section class="slide c1 r2">
  <div class="panel" style="width:138px"></div>
  <h2 class="title light">Our Company</h2>
  <div class="brand"><i></i>KESTRA<br>GRUPPE</div>
  <div class="abs" style="left:12px;top:41px;width:116px">
    <p class="p w">Lorem ipsum dolor sit amet, consectetuer adipiscing elit, sed diam nonummy nibh euismod tincidunt ut laoreet dolore magna aliquam erat volutpat. Ut wisi enim ad minim veniam, quis nostrud exerci tation ullamcorper suscipit lobortis nisl ut aliquip ex ea commodo consequat. Duis autem vel eum iriure dolor in hendrerit in vulputate velit esse molestie consequat, vel illum dolore eu feugiat nulla facilisis at vero eros et accumsan et iusto odio dignissim qui blandit praesent luptatum zzril delenit augue duis dolore te feugait nulla facilisi.</p>
    <p class="p w">Lorem ipsum dolor sit amet, cons ectetuer adipiscing elit, sed diam nonummy nibh euismod tincidunt ut laoreet dolore magna aliquam erat volutpat. Ut wisi enim ad minim veniam, quis nostrud exerci tation ullamcorper suscipit lobortis nisl ut aliquip ex ea commodo consequat. Lorem ipsum dolor sit amet, consecat.</p>
  </div>
  <div class="abs" style="left:152px;top:34px;width:160px;display:flex;flex-direction:column;gap:10px">
    <div style="display:flex;gap:8px;align-items:flex-start"><span class="ring" style="position:static;width:22px;height:22px;flex:none;margin-top:4px"><svg width="10" height="10" viewBox="0 0 10 10"><rect x="1" y="2" width="8" height="5" fill="none" stroke="#2d2a8a" stroke-width=".8"/><circle cx="6" cy="5" r="1.5" fill="none" stroke="#e3131e" stroke-width=".7"/></svg></span><div><div class="h-item" style="font-size:6.5px">Lorem ipsum</div><p class="p" style="margin-top:2px">ipsum dolor sit amet, cons ectetuer adipiscing elit, sed diam nonummy nibh euismod tincidunt ut laoreet dolore magna aliquam erat volutpat. Ut wisi enim ad minim veniam, quis nostrud</p></div></div>
    <div style="display:flex;gap:8px;align-items:flex-start"><span class="ring" style="position:static;width:22px;height:22px;flex:none;margin-top:4px"><svg width="10" height="10" viewBox="0 0 10 10"><path d="M2 6a2 2 0 0 1 1-3.5 2.5 2.5 0 0 1 4.5 0A1.8 1.8 0 0 1 8 6z" fill="#2d2a8a"/><path d="M5 6v3" stroke="#e3131e" stroke-width=".7"/></svg></span><div><div class="h-item" style="font-size:6.5px">Lorem ipsum</div><p class="p" style="margin-top:2px">ipsum dolor sit amet, cons ectetuer adipiscing elit, sed diam nonummy nibh euismod tincidunt ut laoreet dolore magna aliquam erat volutpat. Ut wisi enim ad minim veniam, quis nostrud</p></div></div>
    <div style="display:flex;gap:8px;align-items:flex-start"><span class="ring" style="position:static;width:22px;height:22px;flex:none;margin-top:4px"><svg width="10" height="10" viewBox="0 0 10 10"><path d="M1.5 7.5l2.5-3 2 2 2.5-4" fill="none" stroke="#2d2a8a" stroke-width=".8"/><circle cx="4" cy="4.5" r=".9" fill="#e3131e"/><circle cx="8.5" cy="2.5" r=".9" fill="#e3131e"/></svg></span><div><div class="h-item" style="font-size:6.5px">Lorem ipsum</div><p class="p" style="margin-top:2px">ipsum dolor sit amet, cons ectetuer adipiscing elit, sed diam nonummy nibh euismod tincidunt ut laoreet dolore magna aliquam erat volutpat. Ut wisi enim ad minim veniam, quis nostrud</p></div></div>
  </div>
  <div class="foot light" style="color:#fff">www.kestragruppe.com</div><span class="pg">04</span>
</section>

<!-- 5 Our Education -->
<section class="slide c2 r2">
  <div class="panel" style="width:100%;height:38px"></div>
  <h2 class="title light">Our Education</h2>
  <div class="brand" style="color:#fff"><i></i>KESTRA<br>GRUPPE</div>
  <svg class="abs" style="left:60px;top:52px" width="200" height="82" viewBox="0 0 200 82">
    <g fill="none" stroke="#2d2a8a" stroke-width="1.6">
      <path d="M52 20V6a4 4 0 0 0-4-4H8a4 4 0 0 0-4 4v70a4 4 0 0 0 4 4h44"/>
      <path d="M128 20V6a4 4 0 0 0-4-4H76a4 4 0 0 0-4 4v50"/><path d="M72 70v6a4 4 0 0 0 4 4h48a4 4 0 0 0 4-4V60"/>
      <path d="M148 56V6a4 4 0 0 1 4-4h40a4 4 0 0 1 4 4v70a4 4 0 0 1-4 4h-40a4 4 0 0 1-4-4v-6"/>
      <path d="M52 80a4 4 0 0 0 4-4V50"/>
    </g>
    <g fill="#2d2a8a"><circle cx="52" cy="22" r="2"/><circle cx="72" cy="60" r="2"/><circle cx="128" cy="22" r="2"/><circle cx="148" cy="60" r="2"/></g>
    <g fill="none" stroke="#e3131e" stroke-width=".9"><circle cx="28" cy="15" r="3"/><rect x="97" y="12" width="8" height="6"/><path d="M100 12l1 3 4-3M172 10v8h7M172 17l3-3 2 2 3-4"/></g>
    <g font-family="Montserrat,sans-serif" font-weight="700" font-size="5" fill="#2d2a8a" text-anchor="middle"><text x="28" y="30">IDEA</text><text x="100" y="30">PROMOTION</text><text x="172" y="30">GROWTH</text></g>
    <g font-family="Montserrat,sans-serif" font-size="2.8" fill="#6b6b72" text-anchor="middle">
      <text x="28" y="37">Lorem ipsum dolor sit amet,</text><text x="28" y="40.5">consectetuer adipiscing elit,</text><text x="28" y="44">sed diam nonummy nibh</text><text x="28" y="47.5">euismod tincidunt ut</text><text x="28" y="51">laoreet dolore magna</text><text x="28" y="54.5">aliquam erat volutpat. Ut</text><text x="28" y="58">wisi enim ad minim veniam,</text><text x="28" y="61.5">quis nostrud exerci tation</text><text x="28" y="65">nisl ut aliquip ex ea</text>
      <text x="100" y="37">Lorem ipsum dolor sit amet,</text><text x="100" y="40.5">consectetuer adipiscing elit,</text><text x="100" y="44">sed diam nonummy nibh</text><text x="100" y="47.5">euismod tincidunt ut</text><text x="100" y="51">laoreet dolore magna</text><text x="100" y="54.5">aliquam erat volutpat. Ut</text><text x="100" y="58">wisi enim ad minim veniam,</text><text x="100" y="61.5">quis nostrud exerci tation</text><text x="100" y="65">nisl ut aliquip ex ea</text>
      <text x="172" y="37">Lorem ipsum dolor sit amet,</text><text x="172" y="40.5">consectetuer adipiscing elit,</text><text x="172" y="44">sed diam nonummy nibh</text><text x="172" y="47.5">euismod tincidunt ut</text><text x="172" y="51">laoreet dolore magna</text><text x="172" y="54.5">aliquam erat volutpat. Ut</text><text x="172" y="58">wisi enim ad minim veniam,</text><text x="172" y="61.5">quis nostrud exerci tation</text><text x="172" y="65">nisl ut aliquip ex ea</text>
    </g>
  </svg>
  <p class="p abs" style="left:40px;top:147px;width:240px;text-align:center">Lorem ipsum dolor sit amet, consectetuer adipiscing elit, sed diam nonummy nibh euismod tincidunt ut laoreet dolore magna aliquam erat volutpat. Ut wisi enim ad minim veniam, quis nostrud exerci tation ullamcorper suscipit lobortis nisl ut aliquip ex ea commodo consequat. Duis autem vel eum iriure dolor in hendrerit i</p>
  <div class="foot">www.kestragruppe.com</div><span class="pg">05</span>
</section>

<!-- 6 Our About -->
<section class="slide c3 r2">
  <div class="panel" style="width:138px"></div>
  <h2 class="title light">Our About</h2>
  <div class="brand"><i></i>KESTRA<br>GRUPPE</div>
  <div class="abs" style="left:12px;top:41px;width:116px">
    <p class="p w">Lorem ipsum dolor sit amet, consectetuer adipiscing elit, sed diam nonummy nibh euismod tincidunt ut laoreet dolore magna aliquam erat volutpat. Ut wisi enim ad minim veniam, quis nostrud exerci tation ullamcorper suscipit lobortis nisl ut aliquip ex ea commodo consequat. Duis autem vel eum iriure dolor in hendrerit in vulputate velit esse molestie consequat, vel illum dolore eu feugiat nulla facilisis at vero eros et accumsan et iusto odio dignissim qui blandit praesent luptatum zzril delenit augue duis dolore te feugait nulla facilisi.</p>
    <p class="p w">Lorem ipsum dolor sit amet, cons ectetuer adipiscing elit, sed diam nonummy nibh euismod tincidunt ut laoreet dolore magna aliquam erat volutpat. Ut wisi enim ad minim veniam, quis nostrud exerci tation ullamcorper suscipit lobortis nisl ut aliquip ex ea commodo consequat. Lorem ipsum dolor sit amet, consecat.</p>
  </div>
  <div class="abs" style="left:150px;top:30px;width:160px;display:grid;grid-template-columns:1fr 1fr;row-gap:8px;column-gap:6px">
    <div style="display:flex;flex-direction:column;align-items:center;gap:3px"><span class="ring" style="position:static;width:22px;height:22px"><svg width="10" height="10" viewBox="0 0 10 10"><path d="M3.5 2h3L6 3.5a3 3 0 1 1-2 0z" fill="none" stroke="#e3131e" stroke-width=".8"/></svg></span><span class="cap">LOREM IPSUM</span><p class="p" style="text-align:center">Lorem ipsum dolor sit amet, consectetuer adipiscing elit, sed diam nonummy nibh euismod tincid</p></div>
    <div style="display:flex;flex-direction:column;align-items:center;gap:3px"><span class="ring" style="position:static;width:22px;height:22px"><svg width="10" height="10" viewBox="0 0 10 10"><rect x="1" y="2" width="8" height="6" fill="none" stroke="#2d2a8a" stroke-width=".8"/><path d="M2.5 6.5l2-2 1.5 1 2-2.5" stroke="#e3131e" stroke-width=".8" fill="none"/></svg></span><span class="cap">LOREM IPSUM</span><p class="p" style="text-align:center">Lorem ipsum dolor sit amet, consectetuer adipiscing elit, sed diam nonummy nibh euismod tincid</p></div>
    <div style="display:flex;flex-direction:column;align-items:center;gap:3px"><span class="ring" style="position:static;width:22px;height:22px"><svg width="10" height="10" viewBox="0 0 10 10"><rect x="1.5" y="2" width="7" height="6" fill="#2d2a8a"/><rect x="3" y="4" width="2.5" height="2.5" fill="#e3131e"/></svg></span><span class="cap">LOREM IPSUM</span><p class="p" style="text-align:center">Lorem ipsum dolor sit amet, consectetuer adipiscing elit, sed diam nonummy nibh euismod tincid</p></div>
    <div style="display:flex;flex-direction:column;align-items:center;gap:3px"><span class="ring" style="position:static;width:22px;height:22px"><svg width="10" height="10" viewBox="0 0 10 10"><g fill="none" stroke="#e3131e" stroke-width=".8"><rect x="1.5" y="5" width="1.8" height="3"/><rect x="4.1" y="3.5" width="1.8" height="4.5"/><rect x="6.7" y="2" width="1.8" height="6"/></g></svg></span><span class="cap">LOREM IPSUM</span><p class="p" style="text-align:center">Lorem ipsum dolor sit amet, consectetuer adipiscing elit, sed diam nonummy nibh euismod tincid</p></div>
  </div>
  <div class="foot light" style="color:#fff">www.kestragruppe.com</div><span class="pg">06</span>
</section>

<!-- 7 Text Here (photo) -->
<section class="slide c1 r3">
  <div class="panel" style="width:217px"></div>
  <h2 class="title light">Text Here</h2>
  <div class="brand"><i></i>KESTRA<br>GRUPPE</div>
  <div class="abs" style="left:12px;top:38px;width:128px">
    <p class="p w">Lorem ipsum dolor sit amet, consectetuer adipiscing elit, sed diam nonummy nibh euismod tincidunt ut laoreet dolore magna aliquam erat volutpat.</p>
    <p class="p w">Ut wisi enim ad minim veniam, quis nostrud exerci tation ullamcorper suscipit lobortis nisl ut aliquip ex ea commodo consequat. Duis autem vel eum iriure dolor in hendrerit in vulputate velit esse molestie consequat, vel illum dolore eu feugiat nulla facilisis at vero eros et accumsan e</p>
  </div>
  <div class="abs" style="left:12px;top:103px;width:128px;display:flex;flex-direction:column;gap:8px">
    <div style="display:flex;gap:5px"><span class="num" style="font-size:11px">1.</span><div><div style="font:500 5.5px Montserrat,sans-serif;color:var(--red)">Lorem ipsum</div><p class="p w">Lorem ipsum dolor sit amet, consectetuer adipiscing elit, sed diam nonummy nibh euismod tincid</p></div></div>
    <div style="display:flex;gap:5px"><span class="num" style="font-size:11px">2.</span><div><div style="font:500 5.5px Montserrat,sans-serif;color:var(--red)">Lorem ipsum</div><p class="p w">Lorem ipsum dolor sit amet, consectetuer adipiscing elit, sed diam nonummy nibh euismod tincid</p></div></div>
  </div>
  <div class="photo" role="img" aria-label="Photo of two construction workers in hard hats and safety vests reviewing plans on site" style="left:153px;top:20px;width:107px;height:140px;background:linear-gradient(160deg,#7fa6c8 0%,#c9b070 35%,#e08a2e 55%,#6b6f78 85%,#9aa0a8)"></div>
  <svg class="abs" style="left:287px;top:100px" width="8" height="40"><g fill="#e3131e"><circle cx="1.5" cy="2" r="1"/><circle cx="6" cy="2" r="1"/><circle cx="1.5" cy="8" r="1"/><circle cx="6" cy="8" r="1"/><circle cx="1.5" cy="14" r="1"/><circle cx="6" cy="14" r="1"/><circle cx="1.5" cy="20" r="1"/><circle cx="6" cy="20" r="1"/><circle cx="1.5" cy="26" r="1"/><circle cx="6" cy="26" r="1"/><circle cx="1.5" cy="32" r="1"/><circle cx="6" cy="32" r="1"/><circle cx="1.5" cy="38" r="1"/><circle cx="6" cy="38" r="1"/></g></svg>
  <div class="foot light" style="color:#fff">www.kestragruppe.com</div><span class="pg">07</span>
</section>

<!-- 8 Market Opportunities -->
<section class="slide c2 r3">
  <h2 class="title">Market Opportunities</h2>
  <div class="brand"><i></i>KESTRA<br>GRUPPE</div>
  <div class="abs" style="left:12px;top:38px;width:116px">
    <p class="p">Lorem ipsum dolor sit amet, consectetuer adipiscing elit, sed diam nonummy nibh euismod tincidunt ut laoreet dolore magna aliquam erat volutpat. Ut wisi enim ad minim veniam, quis nostrud exerci tation ullamcorper suscipit lobortis nisl ut aliquip ex ea commodo consequat. Duis autem vel eum iriure dolor in hendrerit i</p>
    <p class="p">Lorem ipsum dolor sit amet, consectetuer adipiscing elit, sed diam nonummy nibh</p>
  </div>
  <svg class="abs" style="left:14px;top:97px" width="104" height="66" viewBox="0 0 104 66">
    <ellipse cx="52" cy="38" rx="50" ry="24" fill="#1e1b63"/>
    <rect x="2" y="30" width="100" height="8" fill="#1e1b63"/>
    <path d="M52 6A50 24 0 0 1 102 30L70 30A18 9 0 0 0 52 21z" fill="#e3131e"/>
    <path d="M102 30A50 24 0 0 1 52 54L52 39A18 9 0 0 0 70 30z" fill="#2d2a8a"/>
    <path d="M52 54A50 24 0 0 1 26 50L42 37A18 9 0 0 0 52 39z" fill="#e3131e"/>
    <path d="M26 50A50 24 0 0 1 52 6L52 21A18 9 0 0 0 42 37z" fill="#2d2a8a"/>
    <ellipse cx="52" cy="30" rx="18" ry="9" fill="#fff"/>
    <g font-family="Roboto Condensed,sans-serif" font-weight="700" font-size="7" fill="#fff"><text x="16" y="33">40%</text><text x="60" y="15">20%</text><text x="83" y="35">20%</text><text x="62" y="50">20%</text></g>
  </svg>
  <div class="abs" style="left:149px;top:35px;font:500 4.5px Montserrat,sans-serif;color:var(--ink)">CONSECTETUER ADIPISCING</div>
  <svg class="abs" style="left:140px;top:43px" width="170" height="84" viewBox="0 0 170 84">
    <g stroke="#ddd" stroke-width=".4"><line x1="12" y1="4" x2="160" y2="4"/><line x1="12" y1="15.5" x2="160" y2="15.5"/><line x1="12" y1="27" x2="160" y2="27"/><line x1="12" y1="38.5" x2="160" y2="38.5"/><line x1="12" y1="50" x2="160" y2="50"/><line x1="12" y1="61.5" x2="160" y2="61.5"/><line x1="160" y1="4" x2="160" y2="73"/></g>
    <line x1="12" y1="73" x2="160" y2="73" stroke="#555" stroke-width=".5"/><line x1="12" y1="4" x2="12" y2="73" stroke="#555" stroke-width=".5"/>
    <g font-family="Montserrat,sans-serif" font-size="4" fill="#444" text-anchor="end"><text x="9" y="5.5">60</text><text x="9" y="17">50</text><text x="9" y="28.5">40</text><text x="9" y="40">30</text><text x="9" y="51.5">20</text><text x="9" y="63">10</text><text x="9" y="74.5">0</text></g>
    <rect x="23" y="25.8" width="16" height="47.2" fill="#e3131e"/>
    <rect x="58" y="6.3" width="16" height="66.7" fill="#2d2a8a"/>
    <rect x="93" y="55.7" width="16" height="17.3" fill="#e3131e"/>
    <rect x="128" y="18.9" width="16" height="54.1" fill="#2d2a8a"/>
    <g font-family="Montserrat,sans-serif" font-size="4" fill="#444" text-anchor="middle"><text x="31" y="81">JAN</text><text x="66" y="81">FEB</text><text x="101" y="81">MAR</text><text x="136" y="81">APR</text></g>
  </svg>
  <div class="abs" style="left:151px;top:136px;width:150px;display:grid;grid-template-columns:1fr 1fr;gap:8px">
    <div><div style="font:500 5px Montserrat,sans-serif;color:var(--navy)"><span class="red">●</span> Lorem ipsum</div><p class="p" style="font-size:2.8px">Lorem ipsum dolor sit amet, consectetuer adipiscing elit, sed diam nonummy nibh euismod tincidunt ut laoreet</p></div>
    <div><div style="font:500 5px Montserrat,sans-serif;color:var(--navy)"><span class="red">●</span> Lorem ipsum</div><p class="p" style="font-size:2.8px">Lorem ipsum dolor sit amet, consectetuer adipiscing elit, sed diam nonummy nibh euismod tincidunt ut laoreet</p></div>
  </div>
  <div class="foot">www.kestragruppe.com</div><span class="pg">08</span>
</section>

<!-- 9 Our Data -->
<section class="slide c3 r3">
  <h2 class="title">Our Data</h2>
  <div class="brand"><i></i>KESTRA<br>GRUPPE</div>
  <div class="abs" style="left:0;top:35px;width:162px;height:126px;background:var(--navy);padding:6px 10px 0 12px;display:flex;flex-direction:column;gap:6px">
    <p class="p w" style="font-size:3.8px"><span class="red">Lorem ipsum :</span> dolor sit amet, consectetuer adipiscing elit, nonummy nibh euismod tincidunt ut laoreet dolore magna</p>
    <p class="p w" style="font-size:3.8px;margin:0"><span class="red">Lorem ipsum :</span> dolor sit amet, consectetuer adipiscing el sed diam nonummy nibh euismod tincidunt ut laoreet dolore magna aliquam erat volutpat. Ut wisi enim ad minut .</p>
    <p class="p w" style="font-size:3.8px;margin:0"><span class="red">Lorem ipsum :</span> dolor sit amet, consectetuer adipis cing elit, sed diam nonummy nibh euismod tinci dunt ut laoreet magna aliquam erat volutpat.</p>
    <p class="p w" style="font-size:3.8px;margin:0"><span class="red">Lorem ipsum :</span> dolor sit amet, consectetuer adipiscing nibh euismod tincidunt ut laoreet dolore magna</p>
    <p class="p w" style="font-size:3.8px;margin:0"><span class="red">Lorem ipsum :</span> dolor sit amet, consectetuer adipis cing elit, sed diam nonummy nibh euismod tinci dunt ut laoreet magna aliquam erat volutpat.</p>
  </div>
  <div class="abs" style="left:173px;top:38px;font:600 8.5px/1.3 Montserrat,sans-serif;color:var(--navy)">WHAT'S A DOMAIN?<br>IT'S THAT NAME UP<br><span class="red" style="font-weight:700">IN THE ADDRESS BAR.</span></div>
  <ul class="abs" style="left:173px;top:82px;list-style:none;font:400 6px/13.2px Montserrat,sans-serif;color:var(--grey)">
    <li><span class="navy">▪</span> Fits your business or products</li>
    <li><span class="navy">▪</span> Is easy to spell and remember</li>
    <li><span class="navy">▪</span> Fits your business or products</li>
    <li><span class="navy">▪</span> Is easy to spell and remember</li>
    <li><span class="navy">▪</span> Fits your business or products</li>
    <li><span class="navy">▪</span> Is easy to spell and remember</li>
  </ul>
  <div class="foot">www.kestragruppe.com</div><span class="pg">09</span>
</section>

<!-- 10 Portfolio Of Projects -->
<section class="slide c1 r4">
  <h2 class="title">Portfolio Of Projects</h2>
  <div class="brand"><i></i>KESTRA<br>GRUPPE</div>
  <div class="abs" style="left:12px;top:39px;width:157px">
    <p class="p" style="text-align:justify">Lorem ipsum dolor sit amet, consectetuer adipiscing elit, sed diam nonummy nibh euismod tincidunt ut laoreet dolore magna aliquam erat volutpat. Ut wisi enim ad minim veniam, quis nostrud exerci tation ullamcorper suscipit lobortis nisl ut aliquip ex ea commodo consequat. Duis autem vel eum iriure dolor in hendrerit in vulputate velit esse</p>
    <p class="p" style="text-align:justify;margin-top:6px">Lorem ipsum dolor sit amet, consectetuer adipiscing elit, sed diam nonummy nibh euismod tincidunt ut laoreet dolore magna aliquam erat volutpat. Ut wisi enim ad minim veniam, quis nostrud exerci tation ullamcorper suscipit lobortis nisl ut aliquip ex ea commodo consequat. Duis autem vel eum iriure dolor in hendrerit in vulputate velit esse</p>
    <div class="bullet" style="margin-top:8px"><b></b><p class="p">Lorem ipsum dolor sit amet, consectetuer adipiscing elit, sed diam nonummy nibh euismod tincidunt ut laoreet dolore magna</p></div>
    <div class="bullet" style="margin-top:6px"><b class="o"></b><p class="p">Lorem ipsum dolor sit amet, consectetuer adipiscing elit, sed diam nonummy nibh euismod tincidunt ut laoreet dolore magna</p></div>
  </div>
  <div class="abs" style="left:176px;top:35px;width:121px;height:122px;border:.8px solid var(--navy)"></div>
  <div class="photo" role="img" aria-label="Photo of an open-plan office with people working at computer desks" style="left:179px;top:38px;width:115px;height:116px;background:linear-gradient(170deg,#e9ecef 0%,#c7ccd2 40%,#7d858f 70%,#3b4048 100%)"></div>
  <div class="foot">www.kestragruppe.com</div><span class="pg">10</span>
</section>

<!-- 11 Text Here (four images) -->
<section class="slide c2 r4">
  <div class="panel" style="width:100%;height:80px"></div>
  <h2 class="title light">Text Here</h2>
  <div class="brand" style="color:#fff"><i></i>KESTRA<br>GRUPPE</div>
  <div class="abs" style="left:12px;top:31px;width:298px">
    <p class="p w">Lorem ipsum dolor sit amet, consectetuer adipiscing elit, sed diam nonummy nibh euismod tincidunt ut laoreet dolore magna aliquam erat volutpat. Ut wisi enim ad minim veniam, quis nostrud exerci tation ullamcorper suscipit lobortis nisl utea commodo consequat. Duis autem vel eum iriure dolor in hendrerit i</p>
    <p class="p w" style="margin-top:5px">Lorem ipsum dolor sit amet, consectetuer adipiscing elit, sed diam nonummy nibh euismod tincidunt ut laoreet dolore magna aliquam erat volutpat. Ut wisi enim ad minim veniam, quis nostrud exerci tation ullamcorper suscipit lobortis nisl utea commodo consequat.</p>
  </div>
  <div class="abs" style="left:16px;top:86px;width:290px;display:grid;grid-template-columns:repeat(4,1fr);gap:7px">
    <div><div role="img" aria-label="Photo of a hand touching a digital interface" style="height:46px;border:.6px solid #bbb;background:linear-gradient(135deg,#0d2a55,#2f6fb5 55%,#c9d9ea)"></div><div style="font:500 5px Montserrat,sans-serif;color:var(--red);margin-top:3px">Lorem ipsum</div><p class="p" style="font-size:2.8px">Lorem ipsum dolor sit amet, consectetuer adipiscing elit, sed diam nonummy nibh euismod tincidunt ut laoreet</p></div>
    <div><div role="img" aria-label="Photo of a business team meeting around a table" style="height:46px;border:.6px solid #bbb;background:linear-gradient(135deg,#f1efe9,#b9a58f 50%,#4d4a55)"></div><div style="font:500 5px Montserrat,sans-serif;color:var(--red);margin-top:3px">Lorem ipsum</div><p class="p" style="font-size:2.8px">Lorem ipsum dolor sit amet, consectetuer adipiscing elit, sed diam nonummy nibh euismod tincidunt ut laoreet</p></div>
    <div><div role="img" aria-label="Image of a glowing blue technology network" style="height:46px;border:.6px solid #bbb;background:radial-gradient(circle at 50% 50%,#6fc3ff,#1a56b3 45%,#07183d)"></div><div style="font:500 5px Montserrat,sans-serif;color:var(--red);margin-top:3px">Lorem ipsum</div><p class="p" style="font-size:2.8px">Lorem ipsum dolor sit amet, consectetuer adipiscing elit, sed diam nonummy nibh euismod tincidunt ut laoreet</p></div>
    <div><div role="img" aria-label="Image of a digital dashboard with connected icons" style="height:46px;border:.6px solid #bbb;background:linear-gradient(135deg,#0b2f45,#2f7f95 50%,#0e3b4f)"></div><div style="font:500 5px Montserrat,sans-serif;color:var(--red);margin-top:3px">Lorem ipsum</div><p class="p" style="font-size:2.8px">Lorem ipsum dolor sit amet, consectetuer adipiscing elit, sed diam nonummy nibh euismod tincidunt ut laoreet</p></div>
  </div>
  <div class="foot">www.kestragruppe.com</div><span class="pg">11</span>
</section>

<!-- 12 Company Summary -->
<section class="slide c3 r4">
  <h2 class="title">Company Summary</h2>
  <div class="brand"><i></i>KESTRA<br>GRUPPE</div>
  <div class="abs" style="left:12px;top:39px;width:118px">
    <p class="p">Lorem ipsum dolor sit amet, consectetuer adipiscing elit, sed diam nonummy nibh euismod tincidunt ut laoreet dolore magna aliquam erat volutpat. Ut wisi enim ad minim veniam</p>
    <p class="p">quis nostrud exerci tation ullamcorper suscipit lobortis nisl ut aliquip ex ea commodo consequat. Duis autem vel</p>
    <div style="margin-top:6px;display:flex;flex-direction:column;gap:6px;padding-left:4px">
      <div><div style="font:500 5px Montserrat,sans-serif;color:var(--red)"><span class="navy">●</span> Lorem ipsum</div><p class="p" style="font-size:2.8px;padding-left:6px">Lorem ipsum dolor sit amet, consectetuer adipiscing elit, sed diam nonummy nibh euismod tincidunt ut laoreet</p></div>
      <div><div style="font:500 5px Montserrat,sans-serif;color:var(--red)"><span class="navy">●</span> Lorem ipsum</div><p class="p" style="font-size:2.8px;padding-left:6px">Lorem ipsum dolor sit amet, consectetuer adipiscing elit, sed diam nonummy nibh euismod tincidunt ut laoreet</p></div>
      <div><div style="font:500 5px Montserrat,sans-serif;color:var(--red)"><span class="navy">●</span> Lorem ipsum</div><p class="p" style="font-size:2.8px;padding-left:6px">Lorem ipsum dolor sit amet, consectetuer adipiscing elit, sed diam nonummy nibh euismod tincidunt ut laoreet</p></div>
    </div>
  </div>
  <svg class="abs" style="left:120px;top:35px" width="198" height="140" viewBox="0 0 198 140">
    <path d="M110 12A58 58 0 0 0 10 62" fill="none" stroke="#2d2a8a" stroke-width="2.2"/>
    <path d="M4 56l6 10 6-10" fill="none" stroke="#2d2a8a" stroke-width="2"/>
    <path d="M18 77A58 58 0 0 0 110 118" fill="none" stroke="#2d2a8a" stroke-width="2.2"/>
    <path d="M110 12A58 58 0 0 1 142 100" fill="none" stroke="#2d2a8a" stroke-width="2.2"/>
    <circle cx="18" cy="77" r="2.5" fill="#2d2a8a"/>
    <circle cx="130" cy="24" r="16" fill="#fff" stroke="#e3131e" stroke-width="3"/><circle cx="130" cy="24" r="10" fill="#e3131e"/>
    <circle cx="144" cy="72" r="14" fill="#fff" stroke="#e3131e" stroke-width="3"/><circle cx="144" cy="72" r="9" fill="#e3131e"/>
    <circle cx="108" cy="115" r="11" fill="#fff" stroke="#e3131e" stroke-width="2.5"/><circle cx="108" cy="115" r="6.5" fill="#e3131e"/>
    <circle cx="36" cy="99" r="9" fill="#fff" stroke="#e3131e" stroke-width="2.5"/><circle cx="36" cy="99" r="5" fill="#e3131e"/>
    <g fill="#e3131e"><rect x="45" y="40" width="2.5" height="10"/><rect x="49" y="44" width="2.5" height="6"/><rect x="53" y="38" width="2.5" height="12"/><rect x="57" y="42" width="2.5" height="8"/></g>
    <g font-family="Montserrat,sans-serif" font-weight="700" fill="#e3131e" font-size="5.5" text-anchor="middle"><text x="52" y="57">MAIN TITLE</text></g>
    <g font-family="Montserrat,sans-serif" font-size="2.6" fill="#6b6b72" text-anchor="middle"><text x="52" y="61">Lorem ipsum dolor sit amet,</text><text x="52" y="64">consectetuer adipiscing elit,</text><text x="52" y="67">sed diam nonummy nibh</text></g>
    <g font-family="Montserrat,sans-serif" font-weight="600" font-size="4.5" fill="#2d2a8a"><text x="160" y="32">Your Title</text><text x="168" y="77">Your Title</text><text x="154" y="107">Your Title</text><text x="64" y="107">Your Title</text></g>
    <g font-family="Montserrat,sans-serif" font-size="2.4" fill="#6b6b72"><text x="160" y="36">Lorem ipsum dolor sit amet,</text><text x="160" y="39">consectetuer adipiscing elit</text><text x="168" y="81">Lorem ipsum dolor sit amet,</text><text x="168" y="84">consectetuer adipiscing elit</text><text x="154" y="111">Lorem ipsum dolor sit amet,</text><text x="154" y="114">consectetuer adipiscing elit</text><text x="64" y="111">Lorem ipsum dolor sit</text><text x="64" y="114">amet, consectetuer</text></g>
    <g font-family="Montserrat,sans-serif" font-weight="700" font-style="normal" font-size="3.5" fill="#2d2a8a"><text x="147" y="10">85%</text><text x="120" y="73">80%</text><text x="57" y="100">50%</text><text x="131" y="130">75%</text></g>
  </svg>
  <div class="foot">www.kestragruppe.com</div><span class="pg">12</span>
</section>

<!-- 13 Timeline Of Roadmap -->
<section class="slide c1 r5">
  <h2 class="title">Timeline Of Roadmap</h2>
  <div class="brand"><i></i>KESTRA<br>GRUPPE</div>
  <svg class="abs" style="left:55px;top:38px" width="280" height="130" viewBox="0 0 280 130">
    <path d="M225 118H170C120 118 95 100 92 88 88 72 135 78 140 56 145 40 100 45 95 58 90 72 60 80 48 66 40 54 68 44 60 35 52 26 40 38 30 30" fill="none" stroke="#2d2a8a" stroke-width="1.6"/>
    <path d="M225 118V92M140 56V40M92 88V70" stroke="#e3131e" stroke-width="1" stroke-dasharray="2 2" fill="none"/>
    <circle cx="225" cy="118" r="2" fill="#e3131e"/>
    <path d="M225 90a24 24 0 1 1 0-48 24 24 0 0 1 0 48z" fill="#fff" stroke="#e3131e" stroke-width="3"/>
    <circle cx="140" cy="38" r="11" fill="#fff" stroke="#e3131e" stroke-width="2.4"/>
    <circle cx="92" cy="62" r="13" fill="#fff" stroke="#e3131e" stroke-width="2.6"/>
    <circle cx="48" cy="38" r="7" fill="#fff" stroke="#e3131e" stroke-width="1.8"/>
    <circle cx="73" cy="21" r="5.5" fill="#fff" stroke="#e3131e" stroke-width="1.5"/>
    <circle cx="30" cy="16" r="4.5" fill="#fff" stroke="#e3131e" stroke-width="1.2"/>
    <g font-family="Montserrat,sans-serif" font-weight="700" fill="#2d2a8a" text-anchor="middle"><text x="225" y="75" font-size="28">1</text><text x="92" y="69" font-size="18">2</text><text x="140" y="44" font-size="15">3</text><text x="48" y="42" font-size="10">4</text><text x="73" y="24.5" font-size="8">5</text><text x="30" y="18.5" font-size="6">6</text></g>
    <g font-family="Montserrat,sans-serif" font-weight="600" font-size="4.3" fill="#2d2a8a"><text x="-2" y="16">Lorem Ipsum</text><text x="80" y="11">Lorem Ipsum</text><text x="151" y="16">Lorem Ipsum</text><text x="28" y="56">Lorem Ipsum</text><text x="128" y="83">Lorem Ipsum</text></g>
    <g font-family="Montserrat,sans-serif" font-size="2.4" fill="#6b6b72"><text x="-2" y="20">Lorem ipsum dolor sit amet,</text><text x="-2" y="23">consectetuer adipiscing elit,</text><text x="80" y="15">Lorem ipsum dolor sit amet,</text><text x="80" y="18">consectetuer adipiscing elit,</text><text x="151" y="20">Lorem ipsum dolor sit amet,</text><text x="151" y="23">consectetuer adipiscing elit,</text><text x="28" y="60">Lorem ipsum dolor sit amet,</text><text x="28" y="63">consectetuer adipiscing elit,</text><text x="128" y="87">Lorem ipsum dolor sit amet,</text><text x="128" y="90">consectetuer adipiscing elit,</text></g>
  </svg>
  <div class="abs" style="left:20px;top:125px;font:600 8.5px Montserrat,sans-serif;color:var(--navy)">FOR 2 YEARS</div>
  <div class="abs" style="left:20px;top:138px;display:flex;gap:22px">
    <div style="display:flex;gap:4px;align-items:center"><span style="width:14px;height:14px;border-radius:50%;background:var(--red);color:#fff;font:700 8px/14px Montserrat,sans-serif;text-align:center">A</span><div><div style="font:500 6.5px Montserrat,sans-serif;color:var(--navy)">2019</div><p class="p" style="font-size:2.4px">Lorem ipsum dolor sit amet, consectetuer adipiscing elit, sed diam</p></div></div>
    <div style="display:flex;gap:4px;align-items:center"><span style="width:14px;height:14px;border-radius:50%;background:var(--red);color:#fff;font:700 8px/14px Montserrat,sans-serif;text-align:center">B</span><div><div style="font:500 6.5px Montserrat,sans-serif;color:var(--navy)">2020</div><p class="p" style="font-size:2.4px">Lorem ipsum dolor sit amet, consectetuer adipiscing elit, sed diam</p></div></div>
  </div>
  <div class="foot">www.kestragruppe.com</div><span class="pg">13</span>
</section>

<!-- 14 Use Cases -->
<section class="slide c2 r5">
  <div class="panel" style="width:105px"></div>
  <h2 class="title light">Use Cases.</h2>
  <div class="brand"><i></i>KESTRA<br>GRUPPE</div>
  <div class="abs" style="left:12px;top:41px;width:84px">
    <p class="p w" style="font-size:3.7px">Lorem ipsum dolor sit amet, consectetuer adipiscing elit, sed diam nonummy nibh euismod tincidunt ut laoreet dolore magna aliquam erat volutpat. Ut wisi enim ad minim veniam, quis nostrud exerci tation ullamcorper suscipit lobortis nisl</p>
    <p class="p w" style="font-size:3.7px">ut aliquip ex ea commodo consequat. Duis autem vel eum iriure dolor in hendrerit in vulputate velit esse molestie consequat, vel illum dolore eu feugiat nulla facilisis at vero eros et accumsan et iusto odio dignissim qui blandit praesent luptatum zzril delenit augue duis dolore te feugait nulla facilisi.</p>
    <p class="p w" style="font-size:3.7px">Lorem ipsum dolor sit amet, cons ectetuer adipiscing elit, sed diam</p>
  </div>
  <div class="abs" style="left:128px;top:22px;width:40px;height:84px;border:.8px solid var(--navy);border-radius:4px;padding:12px 3px 0">
    <div style="font:500 5px/1.1 Montserrat,sans-serif;color:var(--navy)">Lorem<br>ipsum dolor</div>
    <div style="width:6px;height:6px;border:.7px solid var(--red);margin:6px auto"></div>
    <p class="p" style="font-size:2.2px;text-align:center">To introduce the students to the changing landscape of marketing and equip them with knowledge and tools to navigate the digital marketing world.</p>
  </div>
  <div class="abs" style="left:179px;top:47px;width:40px;height:84px;border:.8px solid var(--navy);border-radius:4px;padding:18px 3px 0">
    <div style="font:500 5px/1.1 Montserrat,sans-serif;color:var(--navy)">Dolor sit<br>amet, conse</div>
    <div style="width:6px;height:6px;border:.7px solid var(--red);border-radius:50%;margin:6px auto"></div>
    <p class="p" style="font-size:2.2px;text-align:center">You will learn concepts and ideas in digital marketing as well as how to use different tools and strategies to optimize your digital marketing campaigns.</p>
  </div>
  <div class="abs" style="left:230px;top:73px;width:40px;height:84px;border:.8px solid var(--navy);border-radius:4px;padding:18px 3px 0">
    <div style="font:500 5px/1.1 Montserrat,sans-serif;color:var(--navy)">Consec<br><span class="red">· · · · · ·</span></div>
    <div style="width:6px;height:6px;border:.7px solid var(--red);border-radius:50%;margin:6px auto"></div>
    <p class="p" style="font-size:2.2px;text-align:center">You are required to pass 80% of the evaluation test to obtain the certificate. The evaluation test can only be taken 3 times.</p>
  </div>
  <svg class="abs" style="left:290px;top:58px" width="8" height="30"><g fill="#2d2a8a"><circle cx="2" cy="2" r=".9"/><circle cx="6" cy="2" r=".9"/><circle cx="2" cy="7" r=".9"/><circle cx="6" cy="7" r=".9"/><circle cx="2" cy="12" r=".9"/><circle cx="6" cy="12" r=".9"/><circle cx="2" cy="17" r=".9"/><circle cx="6" cy="17" r=".9"/><circle cx="2" cy="22" r=".9"/><circle cx="6" cy="22" r=".9"/><circle cx="2" cy="27" r=".9"/><circle cx="6" cy="27" r=".9"/></g></svg>
  <svg class="abs" style="left:128px;top:157px" width="22" height="6"><g fill="#e3131e"><circle cx="2" cy="1" r=".9"/><circle cx="6" cy="1" r=".9"/><circle cx="10" cy="1" r=".9"/><circle cx="2" cy="5" r=".9"/><circle cx="6" cy="5" r=".9"/><circle cx="10" cy="5" r=".9"/><circle cx="14" cy="5" r=".9"/><circle cx="18" cy="5" r=".9"/></g></svg>
  <div class="foot light" style="color:#fff">www.kestragruppe.com</div><span class="pg">14</span>
</section>

<!-- 15 Our Company Ipsum -->
<section class="slide c3 r5">
  <h2 class="title">Our Company Ipsum</h2>
  <div class="brand"><i></i>KESTRA<br>GRUPPE</div>
  <svg class="abs" style="left:12px;top:36px" width="300" height="100" viewBox="0 0 300 100">
    <line x1="52" y1="4" x2="52" y2="88" stroke="#888" stroke-width=".5"/>
    <line x1="52" y1="88" x2="256" y2="88" stroke="#2d2a8a" stroke-width=".8" stroke-dasharray="1.5 1.5"/>
    <g font-family="Montserrat,sans-serif" font-size="5" font-weight="600" fill="#2d2a8a"><text x="28" y="18">2019</text><text x="28" y="41">2020</text><text x="28" y="65">2021</text></g>
    <g fill="#e3131e"><circle cx="22" cy="16" r="2.5"/><path d="M22 35v7M19 40a3 3 0 0 0 6 0" stroke="#e3131e" stroke-width="1" fill="none"/><rect x="19.5" y="61" width="5" height="5" rx="1.5"/></g>
    <g>
      <rect x="54" y="9" width="24" height="15" fill="#2d2a8a"/><rect x="78" y="9" width="48" height="15" fill="#e3131e"/><rect x="126" y="9" width="24" height="15" fill="#2d2a8a"/><rect x="150" y="9" width="104" height="15" fill="#e3131e"/>
      <rect x="54" y="32" width="72" height="15" fill="#e3131e"/><rect x="126" y="32" width="51" height="15" fill="#2d2a8a"/><rect x="177" y="32" width="41" height="15" fill="#e3131e"/><rect x="218" y="32" width="36" height="15" fill="#2d2a8a"/>
      <rect x="54" y="56" width="41" height="15" fill="#e3131e"/><rect x="95" y="56" width="61" height="15" fill="#2d2a8a"/><rect x="156" y="56" width="20" height="15" fill="#e3131e"/><rect x="176" y="56" width="78" height="15" fill="#2d2a8a"/>
    </g>
    <g font-family="Montserrat,sans-serif" font-size="5" fill="#fff" text-anchor="middle"><text x="66" y="18">20%</text><text x="102" y="18">40%</text><text x="138" y="18">10%</text><text x="202" y="18">90%</text><text x="90" y="41">50%</text><text x="151" y="41">30%</text><text x="197" y="41">20%</text><text x="236" y="41">20%</text><text x="74" y="65">30%</text><text x="125" y="65">60%</text><text x="166" y="65">10%</text><text x="215" y="65">70%</text></g>
    <g font-family="Montserrat,sans-serif" font-size="4.5" fill="#2d2a8a" text-anchor="middle"><text x="54" y="96">0%</text><text x="74" y="96">10%</text><text x="94" y="96">20%</text><text x="114" y="96">30%</text><text x="134" y="96">40%</text><text x="155" y="96">50%</text><text x="175" y="96">60%</text><text x="195" y="96">70%</text><text x="215" y="96">80%</text><text x="235" y="96">90%</text><text x="254" y="96">100%</text></g>
  </svg>
  <div class="abs" style="left:60px;top:140px;width:230px;display:grid;grid-template-columns:repeat(4,1fr);gap:6px">
    <div><div style="font:500 4.8px Montserrat,sans-serif;color:var(--red)">Lorem Ipsum</div><p class="p" style="font-size:2.6px">Lorem ipsum dolor sit amet, consectetuer adipiscing elit, sed diam nonummy nibh euismod tincid</p></div>
    <div><div style="font:500 4.8px Montserrat,sans-serif;color:var(--red)">Lorem Ipsum</div><p class="p" style="font-size:2.6px">Lorem ipsum dolor sit amet, consectetuer adipiscing elit, sed diam nonummy nibh euismod tincid</p></div>
    <div><div style="font:500 4.8px Montserrat,sans-serif;color:var(--red)">Lorem Ipsum</div><p class="p" style="font-size:2.6px">Lorem ipsum dolor sit amet, consectetuer adipiscing elit, sed diam nonummy nibh euismod tincid</p></div>
    <div><div style="font:500 4.8px Montserrat,sans-serif;color:var(--red)">Lorem Ipsum</div><p class="p" style="font-size:2.6px">Lorem ipsum dolor sit amet, consectetuer adipiscing elit, sed diam nonummy nibh euismod tincid</p></div>
  </div>
  <div class="foot">www.kestragruppe.com</div><span class="pg">15</span>
</section>

<!-- 16 Two Column Text -->
<section class="slide c1 r6">
  <h2 class="title">Two Column Text</h2>
  <div class="brand"><i></i>KESTRA<br>GRUPPE</div>
  <div class="abs" style="left:13px;top:38px;width:298px;display:grid;grid-template-columns:1fr 1fr;gap:10px">
    <div>
      <p class="p" style="text-align:justify">Lorem ipsum dolor sit amet, consectetuer adipiscing elit, sed diam nonummy nibh euismod tincidunt ut laoreet dolore magna aliquam erat volutpat. Ut wisi enim ad minim veniam, quis nostrud exerci tation ullamcorper suscipit lobortis nisl ut aliquip ex ea commodo consequat. Duis autem vel eum iriure dolor in hendrerit in vulputate velit esse</p>
      <p class="p" style="text-align:justify;margin-top:6px">Lorem ipsum dolor sit amet, consectetuer adipiscing elit, sed diam nonummy nibh euismod tincidunt ut laoreet dolore magna aliquam erat volutpat. Ut wisi enim ad minim veniam, quis nostrud exerci tation ullamcorper suscipit lobortis nisl ut aliquip ex ea commodo consequat. Duis autem vel eum iriure dolor in hendrerit in vulputate velit esse</p>
      <div class="bullet" style="margin-top:8px"><b style="border-left-color:var(--navy)"></b><p class="p">Lorem ipsum dolor sit amet, consectetuer adipiscing elit, sed diam nonummy nibh euismod tincidunt ut laoreet dolore magna</p></div>
      <div class="bullet" style="margin-top:6px"><b style="opacity:.6"></b><p class="p">Lorem ipsum dolor sit amet, consectetuer adipiscing elit, sed diam nonummy nibh euismod tincidunt ut laoreet dolore magna</p></div>
    </div>
    <div>
      <p class="p" style="text-align:justify">Lorem ipsum dolor sit amet, consectetuer adipiscing elit, sed diam nonummy nibh euismod tincidunt ut laoreet dolore magna aliquam erat volutpat. Ut wisi enim ad minim veniam, quis nostrud exerci tation ullamcorper suscipit lobortis nisl ut aliquip ex ea commodo consequat. Duis autem vel eum iriure dolor in hendrerit in vulputate velit esse</p>
      <p class="p" style="text-align:justify;margin-top:6px">Lorem ipsum dolor sit amet, consectetuer adipiscing elit, sed diam nonummy nibh euismod tincidunt ut laoreet dolore magna aliquam erat volutpat. Ut wisi enim ad minim veniam, quis nostrud exerci tation ullamcorper suscipit lobortis nisl ut aliquip ex ea commodo consequat. Duis autem vel eum iriure dolor in hendrerit in vulputate velit esse</p>
      <div class="bullet" style="margin-top:8px"><b></b><p class="p">Lorem ipsum dolor sit amet, consectetuer adipiscing elit, sed diam nonummy nibh euismod tincidunt ut laoreet dolore magna</p></div>
      <div class="bullet" style="margin-top:6px"><b class="o"></b><p class="p">Lorem ipsum dolor sit amet, consectetuer adipiscing elit, sed diam nonummy nibh euismod tincidunt ut laoreet dolore magna</p></div>
    </div>
  </div>
  <div class="foot">www.kestragruppe.com</div><span class="pg">16</span>
</section>

<!-- 17 Team Members -->
<section class="slide c2 r6">
  <h2 class="title">Team Members</h2>
  <div class="brand"><i></i>KESTRA<br>GRUPPE</div>
  <div class="abs" style="left:12px;top:36px;width:296px">
    <p class="p">Lorem ipsum dolor sit amet, consectetuer adipiscing elit, sed diam nonummy nibh euismod tincidunt ut laoreet dolore magna aliquam erat volutpat. Ut wisi enim ad minim veniam, quis nostrud exerci tation ullamcorper suscipit lobortis nisl ut aliquip ex ea commodo consequat. Duis autem</p>
    <p class="p">Lorem ipsum dolor sit amet, cons ectetuer adipiscing elit, sed diam nonummy nibh euismod tincidunt ut laoreet dolore magna aliquam erat volutpat.</p>
  </div>
  <div class="abs" style="left:0;top:90px;width:321px;height:75px;background:var(--navy)"></div>
  <div class="abs" style="left:16px;top:77px;width:290px;display:grid;grid-template-columns:repeat(4,1fr);gap:10px;text-align:center">
    <div><div role="img" aria-label="Portrait photo of Jonas Weber" style="width:26px;height:26px;margin:0 auto;border-radius:50%;border:1.5px solid var(--red);background:#c9cdd3"></div><div style="font:700 5.5px Montserrat,sans-serif;color:#fff;margin-top:5px">JONAS WEBER</div><p class="p w" style="font-size:2.6px;margin-top:2px">Ipsum dolor sit amet, cons ectetuer adipiscing elit, sed diam nonummy nibh euismod tincidunt ut laoreet dolore magna aliquam erat volutpat. Ut wisi enim ad minim veniam, quis nostrud</p></div>
    <div><div role="img" aria-label="Portrait photo of Mila Brandt" style="width:26px;height:26px;margin:0 auto;border-radius:50%;border:1.5px solid var(--red);background:#c9cdd3"></div><div style="font:700 5.5px Montserrat,sans-serif;color:#fff;margin-top:5px">MILA BRANDT</div><p class="p w" style="font-size:2.6px;margin-top:2px">Ipsum dolor sit amet, cons ectetuer adipiscing elit, sed diam nonummy nibh euismod tincidunt ut laoreet dolore magna aliquam erat volutpat. Ut wisi enim ad minim veniam, quis nostrud</p></div>
    <div><div role="img" aria-label="Portrait photo of Jonas Weber" style="width:26px;height:26px;margin:0 auto;border-radius:50%;border:1.5px solid var(--red);background:#c9cdd3"></div><div style="font:700 5.5px Montserrat,sans-serif;color:#fff;margin-top:5px">JONAS WEBER</div><p class="p w" style="font-size:2.6px;margin-top:2px">Ipsum dolor sit amet, cons ectetuer adipiscing elit, sed diam nonummy nibh euismod tincidunt ut laoreet dolore magna aliquam erat volutpat. Ut wisi enim ad minim veniam, quis nostrud</p></div>
    <div><div role="img" aria-label="Portrait photo of Mila Brandt" style="width:26px;height:26px;margin:0 auto;border-radius:50%;border:1.5px solid var(--red);background:#c9cdd3"></div><div style="font:700 5.5px Montserrat,sans-serif;color:#fff;margin-top:5px">MILA BRANDT</div><p class="p w" style="font-size:2.6px;margin-top:2px">Ipsum dolor sit amet, cons ectetuer adipiscing elit, sed diam nonummy nibh euismod tincidunt ut laoreet dolore magna aliquam erat volutpat. Ut wisi enim ad minim veniam, quis nostrud</p></div>
  </div>
  <div class="foot">www.kestragruppe.com</div><span class="pg">17</span>
</section>

<!-- 18 Contact -->
<section class="slide c3 r6">
  <div class="abs" role="img" aria-label="Large brand decoration in red and navy" style="left:215px;top:0;width:106px;height:181px;background:linear-gradient(180deg,var(--red) 0%,var(--red) 48%,var(--navy) 52%,var(--navy) 100%)"></div>
  <div class="abs" style="left:20px;top:20px;display:flex;align-items:center;gap:7px">
    <span style="width:32px;height:32px;border-radius:50%;background:var(--red);display:block"></span>
    <span style="font:800 15px/0.95 Montserrat,sans-serif;color:var(--navy)">KESTRA<br>GRUPPE</span>
  </div>
  <div class="abs" style="left:20px;top:99px;font:600 15px/1 Montserrat,sans-serif;color:var(--navy)">Contact <span class="red" style="font-weight:700">Us</span></div>
  <div class="abs" style="left:20px;top:119px;font:400 8px/1 Montserrat,sans-serif;color:var(--navy);display:flex;align-items:center;gap:4px"><svg width="7" height="7" viewBox="0 0 10 10"><circle cx="5" cy="5" r="5" fill="#2d2a8a"/><path d="M3.2 2.8l1 1-.6.8a4 4 0 0 0 1.8 1.8l.8-.6 1 1-.7.8C4.7 7.5 2.5 5.3 2.4 3.5z" fill="#fff"/></svg>0049 301 555 0147</div>
  <div class="abs" style="left:20px;top:134px;font:400 8px/1 Montserrat,sans-serif;color:var(--navy);display:flex;align-items:center;gap:4px"><svg width="7" height="7" viewBox="0 0 10 10"><circle cx="5" cy="5" r="5" fill="#2d2a8a"/><rect x="2.5" y="3.3" width="5" height="3.4" fill="none" stroke="#fff" stroke-width=".7"/><path d="M2.5 3.3L5 5.3l2.5-2" fill="none" stroke="#fff" stroke-width=".7"/></svg>info@kestragruppe.com</div>
  <div class="abs" style="left:20px;top:151px;font:500 8px/1 Montserrat,sans-serif;letter-spacing:3px;color:var(--navy)">www.kestragruppe.com</div>
</section>

</body>
</html>
```